Lantern - Web Design Project

We are seeking to have our website redesigned. Our current webpage is rather dated looking www.lantern-outcomes.com We will be utilizing similar content to explain our services as what is in the website now. We do not see it at a retail portal but rather a website for those inquiring about our services as a reference check so to speak.

We wish to have a look that is considered clean, fresh, contemporary and contains a business savvy vibe.

We prefer isolated white background and also wish to retain the integrity of our Logo and colour scheme.

We are looking for something that doesnt look like it was designed at home on sitemoose. We are hoping to find something that looks like it would reside on a tablet.
Updates

Hello designers!

We apologize for our tardiness as we have been quite preoccupied. We will be extending our invites to the end of January!

Hello All,

Please review our offer once again for updated requirements.  We are hoping to accept a design by months end.

Lantern

Target Market(s)

Business to business clients and Large manufacturers

Industry/Entity Type

Retail

Requirements
Must have
• Existing Logo

There must be an area dedicated to an intro video that will be incorporated on our landing page.

We require design of the other pages as well not only the landing page.

```html
<!DOCTYPE html>
<html lang="en">
<head>
<meta charset="utf-8">
<title>Lantern Performance Group – About Us</title>
<link rel="stylesheet" href="https://fonts.googleapis.com/css2?family=Questrial&family=Open+Sans:wght@400&display=swap">
<style>
  :root {
    --page-bg: #ffffff;
    --panel-bg: #eaeaea;
    --heading-red: #6e1015;
    --body-text: #111111;
    --brand-grey: #4d4a4b;
    --brand-red: #d3201f;
    --nav-bg: #000000;
    --nav-text: #8c8c8c;
    --nav-active-bg: #8d6a6b;
    --nav-active-text: #ffffff;
    --nav-divider: #2a2a2a;
    --backdrop-grey: #bdbdbd;
  }
  * { box-sizing: border-box; margin: 0; padding: 0; }
  html, body {
    width: 1200px; height: 936px; overflow: hidden;
    background: var(--page-bg);
  }
  .page { position: relative; width: 1200px; height: 936px; overflow: hidden; }

  .hero-visual {
    position: absolute; left: 470px; top: 0; width: 730px; height: 810px;
    background: linear-gradient(180deg, #b4b4b4 0%, #c8c8c8 50%, #ececec 85%, #ffffff 100%);
    -webkit-mask-image: linear-gradient(90deg, transparent 0%, #000 35%, #000 88%, transparent 100%);
    mask-image: linear-gradient(90deg, transparent 0%, #000 35%, #000 88%, transparent 100%);
  }

  .brand {
    position: absolute; left: 110px; top: 88px;
    display: flex; align-items: center; gap: 10px;
    font-family: "Questrial", sans-serif;
    font-size: 50px; color: var(--brand-grey); letter-spacing: -1px;
  }
  .brand-dot {
    width: 16px; height: 16px; border-radius: 50%; background: var(--brand-red);
  }

  .about-panel {
    position: absolute; left: 56px; top: 250px; width: 1082px; height: 426px;
    background: var(--panel-bg);
    padding: 50px 100px 0 37px;
  }
  .about-close {
    position: absolute; right: 18px; top: 10px;
    font-family: "Open Sans", sans-serif; font-size: 16px; color: #111;
  }
  .about-title {
    font-family: "Questrial", sans-serif; font-weight: 400;
    font-size: 25px; letter-spacing: -0.5px; color: var(--heading-red);
    margin-bottom: 24px;
  }
  .about-text {
    font-family: "Open Sans", sans-serif; font-size: 13.2px;
    line-height: 21.4px; color: var(--body-text);
    max-width: 960px; margin-bottom: 21.4px;
  }

  .main-nav {
    position: absolute; left: 60px; top: 809px; width: 1077px; height: 113px;
    background: var(--nav-bg);
    display: flex; align-items: center;
  }
  .nav-item {
    height: 71px; display: flex; align-items: center; justify-content: center;
    font-family: "Questrial", sans-serif; font-size: 19px; letter-spacing: -1px;
    color: var(--nav-text); text-decoration: none; white-space: nowrap;
    border-right: 1px solid var(--nav-divider);
  }
  .nav-item:last-child { border-right: none; }
  .nav-home { width: 125px; padding-left: 15px; }
  .nav-who { width: 170px; margin-left: 3px; border-right: none; }
  .nav-performance { width: 300px; margin-left: 4px; border-left: 1px solid var(--nav-divider); }
  .nav-sustain { width: 237px; }
  .nav-cross { flex: 1; }
  .nav-item.is-active {
    background: var(--nav-active-bg); color: var(--nav-active-text);
  }
</style>
</head>
<body>
<div class="page">
  <div class="hero-visual" role="img" aria-label="Header photograph area: a car travelling along a motorway"></div>

  <div class="brand"><span class="brand-dot"></span>lantern</div>

  <section class="about-panel">
    <span class="about-close">×</span>
    <h1 class="about-title">ABOUT US</h1>
    <p class="about-text">With highly experienced performance consultants, trainers and subject matter experts based throughout the North America, Europe, the Middle East and Asia Pacific we offer unrivalled skills and expertise in designing and implementing highly interactive and proven performance solutions, aimed at developing your people and rapidly delivering increased sales and profits.</p>
    <p class="about-text">We do not believe that a cookie cutter approach works in today's environment and that's why we utilize our expertise, people knowledge and various tools to provide a number of customized business solutions.</p>
    <p class="about-text">We will assist you in driving towards improved sales, customer loyalty, performance indicators, processes, staff skill sets and help your business to achieve its long and short term objectives.</p>
    <p class="about-text">We draw on unparalleled experience, our unique global resources and market-leading assets to help clients identify opportunities and build capabilities that underpin high performance. Certainly we will point out the low hanging fruit but consistency is what we aim for.</p>
  </section>

  <nav class="main-nav">
    <a class="nav-item nav-home" href="#">HOME</a>
    <a class="nav-item nav-who is-active" href="#">WHO WE ARE</a>
    <a class="nav-item nav-performance" href="#">PERFORMANCE SOLUTIONS</a>
    <a class="nav-item nav-sustain" href="#">SUSTAIN SOLUTIONS</a>
    <a class="nav-item nav-cross" href="#">CROSS THE LANTERN</a>
  </nav>
</div>
</body>
</html>
```